依頼詳細
お悔みに掲載された方に郵送するダイレクトメールのデザインをお願いしたいと思います。すでにホームページはありますので素材はそちらをいったん利用してもらいたいと思います。
また、レイアウトなどは添付しましたエクセルに記載しています。またスキャンした現在のダイレクトメールが入っています。
記載項目
社名/フリーダイヤル/URL/キャッチコピー/
ロゴなどは現在取り寄せ中。ホームページがあるのでそこから素材をとってください。
サイズ
A4
ページ数
両面
希望イメージ
シンプル 複雑
単色 カラフル
暗い 明るい
日常 高級
遊び心 厳粛
未来的 伝統的
女性的 男性的
希望する色
緑系、グレー系
納品ファイル
• イラストレーター形式 (.ai)
• フォトショップ形式 (.psd)
補足説明
上記のファイルのいずれか。アウトラインのあり・なしのデータをお願いします。
■ 選んだ理由

クライアントの希望にあうデザインだったためです。

■ 提案者全員のお礼・コメント

たくさんのご提案ありがとうございました。またDMやパンフレットなどのデザインコンペなど行った際には、ご参加いただければ幸いです。

宜しくお願い致します。

```html
<!DOCTYPE html>
<html lang="ja">
<head>
<meta charset="UTF-8">
<title>相続税に関する大切なお知らせ</title>
<link href="https://fonts.googleapis.com/css2?family=Noto+Sans+JP:wght@400;500;700;900&display=swap" rel="stylesheet">
<style>
:root{
  --green:#5fae2e;
  --green-dark:#3f8a1c;
  --green-light:#d9ecc6;
  --green-pale:#eef6e4;
  --gray:#e6e8e3;
  --gray-box:#d7dad4;
  --ink:#333;
  --red:#d6261f;
  --cream:#fbf3d6;
  --yellow:#f0d96a;
}
*{margin:0;padding:0;box-sizing:border-box}
html,body{width:859px;height:1200px;overflow:hidden;background:#fff}
body{font-family:"Noto Sans JP",sans-serif;color:var(--ink)}
.sheet{position:relative;width:859px;height:1200px;overflow:hidden;background:#fff}

.hero{position:absolute;left:0;top:0;width:859px;height:430px;background:linear-gradient(180deg,#bfe19e 0%,#e3f1d4 40%,#f3f8ee 80%,#fff 100%)}
.hero-scene{position:absolute;left:0;top:150px;width:859px;height:280px;background:linear-gradient(180deg,rgba(255,255,255,.6),rgba(230,240,225,.5) 60%,rgba(255,255,255,.9))}
.notice-pill{position:absolute;left:50%;top:26px;transform:translateX(-50%);background:var(--green);color:#fff;font-size:16px;font-weight:500;padding:5px 26px;border-radius:20px;white-space:nowrap}
.headline{position:absolute;left:0;top:68px;width:859px;height:72px;background:var(--green);color:#fff;font-size:40px;font-weight:900;text-align:center;line-height:72px;letter-spacing:1px}
.greeting{position:absolute;left:80px;top:185px;width:700px;font-size:17px;line-height:31px;font-weight:500}

.concern{position:absolute;left:60px;top:440px;width:739px;height:440px;background:var(--gray-box);border-radius:14px}
.concern-head{position:absolute;left:150px;top:20px;width:560px;height:112px;background:#fff;border-radius:10px;padding:14px 20px 0 60px}
.concern-head h2{font-size:38px;font-weight:900;color:var(--green-dark);line-height:46px}
.concern-head h2 small{font-size:27px;color:var(--ink)}
.concern-head p{font-size:12px;margin-top:4px}
.advisor{position:absolute;left:20px;top:12px;width:130px;height:150px;background:linear-gradient(180deg,#cfd6c8,#9aa88f);border-radius:50% 50% 12px 12px}
.checklist{position:absolute;left:70px;top:160px;list-style:none}
.checklist li{display:flex;align-items:center;height:54px;font-size:25px;font-weight:700}
.checklist svg{width:30px;height:30px;margin-right:14px;flex:none}
.checklist em{font-style:normal;color:var(--green-dark)}
.checklist strong{color:var(--red)}

.closing{position:absolute;left:70px;top:910px;width:520px;font-size:13px;line-height:22px}
.closing .lead{margin-top:26px;color:var(--green-dark);font-size:19px;font-weight:700}
.bubble{position:absolute;left:635px;top:895px;width:135px;height:112px;border:2px solid var(--green);border-radius:14px;background:#fff;font-size:14px;font-weight:700;text-align:center;padding-top:18px;line-height:22px}
.bubble::after{content:"";position:absolute;right:-12px;top:60px;border:8px solid transparent;border-left:12px solid var(--green)}
.staff{position:absolute;left:778px;top:950px;width:62px;height:110px;background:linear-gradient(180deg,#c8d2c0,#8a9a80);border-radius:30px 30px 6px 6px}

.footer{position:absolute;left:0;top:1072px;width:859px;height:128px;background:var(--green-light)}
.reserve-pill{position:absolute;left:14px;top:14px;background:var(--green);color:#fff;font-size:15px;font-weight:700;padding:5px 14px;border-radius:16px}
.phone{position:absolute;left:14px;top:50px;display:flex;align-items:center;color:var(--green-dark);font-size:44px;font-weight:900;letter-spacing:1px}
.phone svg{width:40px;height:40px;margin-right:6px}
.phone-note{position:absolute;left:14px;top:104px;font-size:12px;font-weight:500}
.office{position:absolute;left:355px;top:16px;font-size:11px}
.office-name{position:absolute;left:355px;top:32px;font-size:20px;font-weight:700}
.hours{position:absolute;left:530px;top:62px;font-size:13px;font-weight:700;line-height:19px}
.call-note{position:absolute;left:400px;top:98px;background:var(--green);color:#fff;font-size:13px;padding:3px 16px;border-radius:12px}
.coupon{position:absolute;left:650px;top:20px;width:196px;height:100px;background:var(--cream);border:2px dashed var(--yellow);padding:10px 12px}
.coupon h3{font-size:20px;font-weight:900;color:var(--ink);line-height:26px}
.coupon p{font-size:11px;margin-top:8px}
</style>
</head>
<body>
<main class="sheet">
  <section class="hero">
    <div class="hero-scene" role="img" aria-label="青空と緑の草木の穏やかな風景写真"></div>
    <p class="notice-pill">相続税や名義変更手続に関する大切なお知らせ</p>
    <h1 class="headline">平成27年より相続税が増税されました。</h1>
    <p class="greeting">このたびはご親族様の訃報、心よりお悔やみ申し上げます。<br>当事務所は、新聞のお悔やみ欄を拝見しお送りさせていただきました。<br>喪中にもかかわらずこのようなお便りをお送りさせて頂いたことを<br>お気分を害されましたらご容赦ください。<br>弊社といたしましては、少しでも相続に対するご家族様の不安や<br>悩み負担が軽くなればとの想いでお便りさせていただきました。</p>
  </section>

  <section class="concern">
    <div class="concern-head">
      <h2>相続税・名義変更<small>などで</small><br>お困りではありませんか?</h2>
      <p>（一部の手続きは3か月以内に行わなければいけないものがございます）</p>
    </div>
    <div class="advisor" role="img" aria-label="相談員のイラスト"></div>
    <ul class="checklist">
      <li><svg viewBox="0 0 30 30"><rect x="2" y="4" width="24" height="24" fill="#fff" stroke="#d6261f" stroke-width="2"/><path d="M7 15l6 7L28 4" fill="none" stroke="#d6261f" stroke-width="4"/></svg>周りに<em>相談</em>する人がいない</li>
      <li><svg viewBox="0 0 30 30"><rect x="2" y="4" width="24" height="24" fill="#fff" stroke="#d6261f" stroke-width="2"/><path d="M7 15l6 7L28 4" fill="none" stroke="#d6261f" stroke-width="4"/></svg>相続税がかかるかの<em>判断だけでも</em>してほしい</li>
      <li><svg viewBox="0 0 30 30"><rect x="2" y="4" width="24" height="24" fill="#fff" stroke="#d6261f" stroke-width="2"/><path d="M7 15l6 7L28 4" fill="none" stroke="#d6261f" stroke-width="4"/></svg>相続は初めてで何をしたらいいか<em>わからない</em></li>
      <li><svg viewBox="0 0 30 30"><rect x="2" y="4" width="24" height="24" fill="#fff" stroke="#d6261f" stroke-width="2"/><path d="M7 15l6 7L28 4" fill="none" stroke="#d6261f" stroke-width="4"/></svg>自分で手続きをするのが<strong>不安</strong>だ</li>
      <li><svg viewBox="0 0 30 30"><rect x="2" y="4" width="24" height="24" fill="#fff" stroke="#d6261f" stroke-width="2"/><path d="M7 15l6 7L28 4" fill="none" stroke="#d6261f" stroke-width="4"/></svg>役所のあいている平日になかなか<em>休めない</em></li>
    </ul>
  </section>

  <section class="closing">
    <p>ご遺族様の不安や悩みをお聞かせください。<br>経験豊富な税理士・行政書士・司法書士が連携し、初回のご相談は無料です。<br>相続税の申告から名義変更まで、まとめてお任せいただけます。<br>複雑な問題も専門家がわかりやすくご説明いたします。</p>
    <p class="lead">あなたにとって一番よい解決方法をご提案いたします。</p>
  </section>
  <div class="bubble">総勢10名体制で<br>お客様を<br>サポートします。</div>
  <div class="staff" role="img" aria-label="スタッフのイラスト"></div>

  <footer class="footer">
    <p class="reserve-pill">ご予約はこちらから</p>
    <p class="phone"><svg viewBox="0 0 40 40"><rect x="2" y="6" width="36" height="28" rx="6" fill="#3f8a1c"/><path d="M13 13c0 8 6 14 14 14l2-4-4-2-2 2c-3-1-5-3-6-6l2-2-2-4z" fill="#fff"/></svg>0120-418-275</p>
    <p class="phone-note">（土日祝日も対応いたします）</p>
    <p class="office">〒950-0000 新潟県緑ヶ丘市中央2丁目8-14</p>
    <p class="office-name">緑ヶ丘相続サポートセンター</p>
    <p class="hours">【受付時間】<br>8:00〜19:00</p>
    <p class="call-note">お気軽にご連絡ください!</p>
    <div class="coupon">
      <h3>ご相談<br>無料チケット</h3>
      <p>有効期限　　　年　　月　　日</p>
    </div>
  </footer>
</main>
</body>
</html>
```